Brightline Healthcare Coming Soon Sign

I need a large (10 x5) road banner announcing the construction of our new medical practice at 3187 Marlowe Ferry Road in John's Island. The name of our practice is Brightline Healthcare and we thought it would be fund to nick name it the "Brightline Waystation". We'd like the tagline to read - "There's nothing healthy about driving an hour to see your doctor. So we're coming to you." Opening Late 2025 I have attached three logos as we have two other practices (Brightline Urgent and Brightline Aesthetics ) that should be present on the bottom of the sign but the main business is Brightline Healthcare. For more information on our look/feel visit our website www.goplainwell-example.com (which should be somewhere on the banner as well)
Updates

The signage needs to say Coming Late Fall 2025!

Target Market(s)

Drive By traffic must be made aware that we are coming soon

Industry/Entity Type

Healthcare

Requirements
Nice to have
• Western Theme

```html
<!DOCTYPE html>
<html lang="en">
<head>
<meta charset="utf-8">
<title>Brightline Healthcare – Coming Late Fall 2025</title>
<link rel="stylesheet" href="https://fonts.googleapis.com/css2?family=Roboto+Condensed:wght@500;600;700&display=swap">
<style>
  :root {
    --navy: #1f2d5c;
    --navy-deep: #1a2750;
    --sky: #5aa8de;
    --white: #ffffff;
    --alert-red: #e8412f;
    --rose: #e6217f;
    --backdrop: #e9ecf0;
  }
  * { margin: 0; padding: 0; box-sizing: border-box; }
  html, body {
    width: 1200px; height: 798px; overflow: hidden;
    background: var(--backdrop);
    font-family: "Roboto Condensed", sans-serif;
  }
  .banner {
    position: absolute; left: 40px; top: 113px;
    width: 1120px; height: 571px;
    background: var(--white);
    border: 2px solid var(--navy);
    padding: 8px;
  }
  .banner-panel {
    position: relative; width: 100%; height: 100%;
    background: var(--navy); overflow: hidden;
  }
  .base-wave { position: absolute; inset: 0; width: 100%; height: 100%; }
  .brand-mark {
    position: absolute; left: 26px; top: 50px;
    display: flex; align-items: center; gap: 14px;
  }
  .brand-mark .dot {
    width: 22px; height: 22px; background: var(--sky);
  }
  .brand-mark .name {
    color: var(--white); font-weight: 700; font-size: 32px;
    letter-spacing: 3px; text-transform: uppercase;
  }
  .launch-pill {
    position: absolute; right: 0; top: 45px;
    height: 54px; padding: 0 48px 0 18px;
    background: var(--alert-red);
    border-radius: 14px 0 0 14px;
    color: var(--white); font-weight: 600; font-size: 29px;
    display: flex; align-items: center;
  }
  .tagline {
    position: absolute; left: 0; right: 0; top: 178px;
    text-align: center; color: var(--white);
    font-weight: 600; font-size: 41px; line-height: 58px;
  }
  .sister-practices {
    position: absolute; left: 0; right: 0; top: 378px;
    display: flex; justify-content: center; align-items: center; gap: 34px;
  }
  .practice { display: flex; align-items: center; gap: 10px; }
  .practice .mark-circle { width: 34px; height: 34px; border-radius: 50%; background: var(--rose); }
  .practice .mark-square { width: 22px; height: 22px; background: var(--white); }
  .practice .name {
    color: var(--white); font-weight: 700; font-size: 24px;
    letter-spacing: 2px; text-transform: uppercase;
  }
  .contact-row {
    position: absolute; left: 26px; right: 20px; bottom: 16px;
    display: flex; justify-content: space-between; align-items: center;
    color: var(--navy); font-weight: 600; font-size: 26px;
  }
  .contact-item { display: flex; align-items: center; gap: 12px; }
  .contact-item svg { display: block; }
</style>
</head>
<body>
  <div class="banner">
    <div class="banner-panel">
      <svg class="base-wave" viewBox="0 0 1100 551" preserveAspectRatio="none" aria-hidden="true">
        <path d="M0 365 Q550 559 1100 365 L1100 551 L0 551 Z" fill="var(--sky)"/>
        <path d="M0 382 Q550 566 1100 382 L1100 551 L0 551 Z" fill="var(--navy-deep)"/>
        <path d="M0 392 Q550 572 1100 392 L1100 551 L0 551 Z" fill="var(--sky)"/>
      </svg>

      <div class="brand-mark">
        <span class="dot"></span>
        <span class="name">Brightline Healthcare</span>
      </div>

      <div class="launch-pill">Coming Late Fall 2025!</div>

      <p class="tagline">There's Nothing Healthy About Driving An<br>Hour To See Your Doctor. So We're Coming To You.</p>

      <div class="sister-practices">
        <div class="practice">
          <span class="mark-circle"></span>
          <span class="name">Brightline Aesthetics</span>
        </div>
        <div class="practice">
          <span class="mark-square"></span>
          <span class="name">Brightline Urgent</span>
        </div>
      </div>

      <div class="contact-row">
        <div class="contact-item">
          <svg width="26" height="40" viewBox="0 0 26 40" aria-hidden="true">
            <path d="M13 1C6.4 1 1 6.3 1 13c0 9 12 26 12 26s12-17 12-26C25 6.3 19.6 1 13 1z" fill="var(--navy)"/>
            <circle cx="13" cy="13" r="5" fill="var(--sky)"/>
          </svg>
          <span>3187 Marlowe Ferry Road in John's Island</span>
        </div>
        <div class="contact-item">
          <svg width="32" height="32" viewBox="0 0 32 32" aria-hidden="true" fill="none" stroke="var(--navy)" stroke-width="2">
            <circle cx="16" cy="16" r="14"/>
            <ellipse cx="16" cy="16" rx="6" ry="14"/>
            <line x1="2" y1="16" x2="30" y2="16"/>
            <path d="M4.5 9h23M4.5 23h23"/>
          </svg>
          <span>www.goplainwell-example.com</span>
        </div>
      </div>
    </div>
  </div>
</body>
</html>
```